New Infographic Design Project

Hi, I have another project to work on if you are interested. It is a horizontal style infographic with 6 steps. It should display the step Number (1-6), Title, and an Icon.

Step 1 - Strong Phone Interview
Step 2 - Pre-Employment
Step 3 - Prep & Do In-Person Interview
Step 4 - Second Interview
Step 5 - Reference Checks
Step 6 - Job Offer

More flexible on colors with this one, but keep it professional.

```html
<!DOCTYPE html>
<html lang="en">
<head>
<meta charset="utf-8">
<title>Hiring Process – 6 Steps</title>
<link href="https://fonts.googleapis.com/css2?family=Montserrat:wght@500&family=Roboto+Condensed:wght@700&display=swap" rel="stylesheet">
<style>
  :root {
    --card: #ffffff;
    --ink: #555555;
    --icon: #555555;
    --rule: #4f4f4f;
    --tint-lavender: #ecdcf8;
    --tint-mint: #dcf9de;
    --tint-peach: #fde9c9;
    --tint-cyan: #cdf5f9;
    --tint-pink: #fde0ec;
    --tint-aqua: #d2f7ea;
  }
  * { box-sizing: border-box; margin: 0; padding: 0; }
  html, body {
    width: 1200px;
    height: 442px;
    overflow: hidden;
    background: var(--card);
  }
  .infographic {
    position: relative;
    width: 1200px;
    height: 442px;
    background: var(--card);
  }
  .step {
    position: absolute;
    top: 0;
    width: 180px;
    margin-left: -90px;
    text-align: center;
    color: var(--ink);
  }
  .step__icon {
    display: block;
    width: 112px;
    height: 110px;
    margin: 80px auto 0;
  }
  .step__number {
    margin-top: 38px;
    font-family: "Montserrat", sans-serif;
    font-weight: 500;
    font-size: 24px;
    line-height: 28px;
    letter-spacing: 1px;
  }
  .step__rule {
    width: 104px;
    height: 0;
    margin: 10px auto 0;
    border-top: 1.5px solid var(--rule);
  }
  .step__title {
    margin-top: 12px;
    font-family: "Roboto Condensed", sans-serif;
    font-weight: 700;
    font-size: 18.5px;
    line-height: 22px;
    text-transform: uppercase;
  }
  .icon-label {
    font-family: "Roboto Condensed", sans-serif;
    font-weight: 700;
  }
</style>
</head>
<body>
<main class="infographic">

  <section class="step" style="left:112px">
    <svg class="step__icon" viewBox="0 0 100 100" role="img" aria-label="Icon: phone call with question mark">
      <path d="M8 52 C4 30 22 12 48 10 C72 8 88 14 86 40 C84 66 92 88 66 92 C40 96 12 80 8 52 Z" fill="var(--tint-lavender)"/>
      <path transform="translate(10,8) scale(3)" fill="var(--icon)" d="M6.62 10.79c1.44 2.83 3.76 5.14 6.59 6.59l2.2-2.2c.27-.27.67-.36 1.02-.24 1.12.37 2.33.57 3.57.57.55 0 1 .45 1 1V20c0 .55-.45 1-1 1-9.39 0-17-7.61-17-17 0-.55.45-1 1-1h3.5c.55 0 1 .45 1 1 0 1.25.2 2.45.57 3.57.11.35.03.74-.25 1.02l-2.2 2.2z"/>
      <circle cx="80" cy="80" r="17" fill="var(--icon)"/>
      <text x="80" y="89" text-anchor="middle" font-size="26" fill="#ffffff" class="icon-label">?</text>
    </svg>
    <div class="step__number">01</div>
    <div class="step__rule"></div>
    <h2 class="step__title">Strong<br>Phone<br>Interview</h2>
  </section>

  <section class="step" style="left:300px">
    <svg class="step__icon" viewBox="0 0 100 100" role="img" aria-label="Icon: jobs newspaper">
      <path d="M6 58 C2 34 20 14 46 12 C66 10 78 28 84 44 C90 56 104 60 92 70 C78 80 70 98 44 96 C22 94 8 78 6 58 Z" fill="var(--tint-mint)"/>
      <g transform="rotate(-8 50 56)">
        <rect x="14" y="22" width="72" height="70" rx="4" fill="var(--icon)"/>
        <text x="50" y="50" text-anchor="middle" font-size="22" fill="var(--tint-mint)" class="icon-label">JOBS</text>
        <rect x="22" y="58" width="24" height="4" fill="var(--tint-mint)"/>
        <rect x="22" y="67" width="24" height="4" fill="var(--tint-mint)"/>
        <rect x="22" y="76" width="24" height="4" fill="var(--tint-mint)"/>
        <rect x="52" y="58" width="26" height="22" fill="var(--tint-mint)"/>
      </g>
    </svg>
    <div class="step__number">02</div>
    <div class="step__rule"></div>
    <h2 class="step__title">Pre -<br>Employment</h2>
  </section>

  <section class="step" style="left:493px">
    <svg class="step__icon" viewBox="0 0 100 100" role="img" aria-label="Icon: office building">
      <path d="M2 24 C10 14 30 20 50 18 C70 16 96 18 100 34 C102 46 88 54 80 66 C70 84 62 98 42 94 C22 90 18 70 10 54 C4 42 -4 32 2 24 Z" fill="var(--tint-peach)"/>
      <path d="M28 14 L62 4 L84 12 L84 84 L28 84 Z" fill="var(--icon)"/>
      <g fill="var(--tint-peach)">
        <rect x="38" y="22" width="14" height="8"/><rect x="60" y="22" width="14" height="8"/>
        <rect x="38" y="36" width="14" height="8"/><rect x="60" y="36" width="14" height="8"/>
        <rect x="38" y="50" width="14" height="8"/><rect x="60" y="50" width="14" height="8"/>
        <rect x="49" y="68" width="14" height="16"/>
      </g>
    </svg>
    <div class="step__number">03</div>
    <div class="step__rule"></div>
    <h2 class="step__title">Prep Do<br>In-Person<br>Interview</h2>
  </section>

  <section class="step" style="left:694px">
    <svg class="step__icon" viewBox="0 0 100 100" role="img" aria-label="Icon: magnifying glass">
      <path d="M4 60 C2 46 18 40 34 30 C50 20 58 4 76 6 C92 8 94 30 90 50 C86 70 76 80 56 82 C34 84 6 78 4 60 Z" fill="var(--tint-cyan)"/>
      <circle cx="40" cy="38" r="27" fill="none" stroke="var(--icon)" stroke-width="9"/>
      <line x1="60" y1="58" x2="86" y2="84" stroke="var(--icon)" stroke-width="13" stroke-linecap="round"/>
    </svg>
    <div class="step__number">04</div>
    <div class="step__rule"></div>
    <h2 class="step__title">Second<br>Interview</h2>
  </section>

  <section class="step" style="left:889px">
    <svg class="step__icon" viewBox="0 0 100 100" role="img" aria-label="Icon: stack of documents">
      <path d="M8 46 C12 28 30 22 48 18 C66 14 84 -4 92 14 C98 30 94 60 88 80 C82 98 68 104 52 92 C36 80 4 70 8 46 Z" fill="var(--tint-pink)"/>
      <path d="M20 16 L20 92 L76 92" fill="none" stroke="var(--icon)" stroke-width="4"/>
      <path d="M28 8 L76 8 L86 18 L86 84 L28 84 Z" fill="var(--icon)"/>
      <g fill="var(--tint-pink)">
        <rect x="48" y="22" width="18" height="18" rx="2"/>
        <rect x="38" y="50" width="40" height="4"/>
        <rect x="38" y="60" width="40" height="4"/>
        <rect x="38" y="70" width="24" height="4"/>
      </g>
    </svg>
    <div class="step__number">05</div>
    <div class="step__rule"></div>
    <h2 class="step__title">Reference<br>Checks</h2>
  </section>

  <section class="step" style="left:1083px">
    <svg class="step__icon" viewBox="0 0 100 100" role="img" aria-label="Icon: job listing with magnifying glass">
      <path d="M4 36 C6 18 30 8 52 6 C74 4 96 12 98 32 C100 50 80 58 72 74 C64 90 52 104 40 92 C28 80 2 58 4 36 Z" fill="var(--tint-aqua)"/>
      <rect x="8" y="16" width="84" height="58" rx="4" fill="var(--icon)"/>
      <text x="48" y="42" text-anchor="middle" font-size="26" fill="var(--tint-aqua)" class="icon-label">JOB</text>
      <rect x="16" y="50" width="22" height="4" fill="var(--tint-aqua)"/>
      <rect x="16" y="59" width="22" height="4" fill="var(--tint-aqua)"/>
      <circle cx="62" cy="58" r="17" fill="var(--icon)" stroke="var(--tint-aqua)" stroke-width="3"/>
      <line x1="75" y1="71" x2="86" y2="84" stroke="var(--icon)" stroke-width="7" stroke-linecap="round"/>
    </svg>
    <div class="step__number">06</div>
    <div class="step__rule"></div>
    <h2 class="step__title">Job Offer</h2>
  </section>

</main>
</body>
</html>
```